Business card/Stationary for mobile ultrasound company
Corvin Ultrasound Services, LLC
Business card/Stationary for mobile ultrasound company -
Creative Brief
Use specific fonts
can use a combination of fonts similar to logo
Professional
Tessa Quillon RDMS, RVT, RCS
Owner
P.O. Box 482 Larkfield, NM 88299-0482
4quillons@mailnest.example
I am currently getting a website designed so i will add a web address and an updated email address specifically for the business. I am torn as to use a one sided or 2 sided card. So im open. I would rather not have the address on the card. Thanks
Innovative mobile technology focused on improving the QUALITY of patient care. (The wording can change but along this idea)

```html
<!DOCTYPE html>
<html lang="en">
<head>
<meta charset="utf-8">
<title>Corvin Ultrasound Services – Business Card</title>
<link href="https://fonts.googleapis.com/css2?family=Open+Sans:ital,wght@0,400;0,600;0,700;1,700&display=swap" rel="stylesheet">
<style>
  :root {
    --backdrop: #3a3a3a;
    --card-black: #0b0b0b;
    --olive: #6e6b33;
    --text-light: #ffffff;
    --text-soft: #ecebdc;
  }
  html, body {
    margin: 0;
    padding: 0;
    width: 1200px;
    height: 780px;
    overflow: hidden;
    background: var(--backdrop);
    font-family: "Open Sans", Arial, sans-serif;
  }
  .stage {
    position: relative;
    width: 1200px;
    height: 780px;
  }
  .card {
    position: absolute;
    left: 100px;
    top: 90px;
    width: 1000px;
    height: 600px;
    border-radius: 36px;
    overflow: hidden;
    background: var(--card-black);
    box-shadow: 0 14px 40px rgba(0,0,0,0.45);
  }
  .card-shapes {
    position: absolute;
    inset: 0;
  }
  .brand {
    position: absolute;
    left: 0;
    right: 0;
    top: 110px;
    text-align: center;
    color: var(--text-light);
    font-weight: 400;
  }
  .brand-name {
    font-size: 96px;
    line-height: 1;
    letter-spacing: 2px;
  }
  .brand-sub {
    font-size: 30px;
    margin-top: 6px;
    letter-spacing: 0.5px;
  }
  .holder {
    position: absolute;
    left: 58px;
    top: 498px;
    width: 420px;
    color: var(--text-light);
  }
  .holder-name {
    font-size: 27px;
    font-weight: 700;
    font-style: italic;
    white-space: nowrap;
  }
  .holder-creds {
    font-size: 22px;
  }
  .holder-role {
    text-align: right;
    font-size: 22px;
    font-weight: 700;
    margin-top: 4px;
  }
  .divider {
    position: absolute;
    left: 518px;
    top: 398px;
    width: 2px;
    height: 168px;
    background: var(--text-light);
  }
  .contact {
    position: absolute;
    left: 546px;
    top: 404px;
    color: var(--text-soft);
    font-size: 20px;
    line-height: 1.3;
  }
  .contact-address { margin-bottom: 12px; }
  .contact-row {
    display: flex;
    align-items: center;
    gap: 12px;
    margin-top: 8px;
  }
  .contact-icon {
    width: 20px;
    height: 20px;
    flex: none;
  }
</style>
</head>
<body>
<main class="stage">
  <section class="card" aria-label="Business card">
    <svg class="card-shapes" viewBox="0 0 1000 600" preserveAspectRatio="none" aria-hidden="true">
      <defs>
        <linearGradient id="oliveFill" x1="0" y1="0" x2="0" y2="1">
          <stop offset="0" stop-color="#77743a"/>
          <stop offset="1" stop-color="#5b5928"/>
        </linearGradient>
        <linearGradient id="greyBand" x1="0" y1="0" x2="1" y2="0">
          <stop offset="0" stop-color="#b5b5b5"/>
          <stop offset="0.6" stop-color="#8a8a8a"/>
          <stop offset="1" stop-color="#5a5a5a"/>
        </linearGradient>
      </defs>
      <path d="M0 318 C 220 300, 420 330, 600 340 C 780 350, 900 320, 1000 290 L1000 360 L0 370 Z" fill="url(#greyBand)"/>
      <path d="M0 362 C 240 340, 460 372, 640 372 C 800 372, 920 345, 1000 318 L1000 600 L0 600 Z" fill="url(#oliveFill)"/>
    </svg>

    <div class="brand">
      <div class="brand-name">Corvin</div>
      <div class="brand-sub">Ultrasound Services, LLC</div>
    </div>

    <div class="holder">
      <div class="holder-name">Tessa Quillon <span class="holder-creds">RDMS, RVT, RCS</span></div>
      <div class="holder-role">Owner</div>
    </div>

    <div class="divider"></div>

    <div class="contact">
      <div class="contact-address">P.O. Box 482<br>Larkfield, NM 88299-0482</div>
      <div class="contact-row">
        <svg class="contact-icon" viewBox="0 0 24 24" aria-hidden="true">
          <path d="M6.6 10.8c1.4 2.8 3.8 5.1 6.6 6.6l2.2-2.2c.3-.3.7-.4 1-.2 1.1.4 2.3.6 3.6.6.6 0 1 .4 1 1V20c0 .6-.4 1-1 1C10.6 21 3 13.4 3 4c0-.6.4-1 1-1h3.5c.6 0 1 .4 1 1 0 1.3.2 2.5.6 3.6.1.3 0 .7-.2 1l-2.3 2.2z" fill="#ffffff"/>
        </svg>
        <span>575-555-0148</span>
      </div>
      <div class="contact-row">
        <svg class="contact-icon" viewBox="0 0 24 24" aria-hidden="true">
          <text x="12" y="18" text-anchor="middle" font-family="Open Sans, Arial, sans-serif" font-size="20" font-weight="700" fill="#ffffff">@</text>
        </svg>
        <span>4quillons@mailnest.example</span>
      </div>
    </div>
  </section>
</main>
</body>
</html>
```